quiet meadow therapy (QMT)

I need to build a website for my therapy business.
There are two parts to the website
on the landing page; they choose whether they are therapists making a referral or patients needing more information.
After that, they are taken to their respective pages.
There is the textual information and a referral form on the therapist page, and on the patient page, the text is a bit different, and there will be a booking page on the patient page.
Visually minimal, it's a therapeutic website. I want it clean, clinical, and modern
colors: greenish blue or maybe orangish
PHP/html code
Updates

Hi everyone
I'm very sorry for the lack of responses to your designs. I am trying to work it out, but this platform has been a challenge for me.
I appreciate everyone's efforts, and I am unsure how to rate designs and move forward with the ones I like. There is a 5-star rating, but I don't understand how I'm supposed to politely say that it is not it without feeling like I'm going to affect someone's future rating negatively.
Please understand me. Thank you

Designs look the same

Target Market(s)

therapy and stress management

Industry/Entity Type

stress management therapy

Coding

Coded - Design and coding required

Number of Pages Required

5+ page

Font styles to use
Serif

Colors
0094D4
00A9DD
6FCCEA
C7EBF8
E9F6FB
00AB8E
00BBA5
67D7C9
C6EFE9
E9F9F6

Requirements
Must have
• landing page that that have 2 options. one for therapist another for patient

```html
<!DOCTYPE html>
<html lang="en">
<head>
<meta charset="utf-8">
<title>Quiet Meadow Therapy</title>
<link rel="stylesheet" href="https://fonts.googleapis.com/css2?family=Merriweather:wght@300;400;700&family=Montserrat:wght@400;500;600;700&display=swap">
<style>
:root{
  --navy:#174a6c;
  --navy-dark:#0f3b59;
  --orange:#f39200;
  --teal:#1db1a2;
  --teal-soft:#e9f6f5;
  --ink:#2f2f2f;
  --muted:#555;
  --line:#e3e3e3;
  --white:#fff;
}
*{margin:0;padding:0;box-sizing:border-box}
html,body{width:1200px;height:3817px;overflow:hidden}
body{position:relative;background:var(--white);font-family:'Montserrat',sans-serif;color:var(--ink)}
.abs{position:absolute}
.serif{font-family:'Merriweather',serif}

/* header */
.topbar{top:20px;left:798px;font-size:12px;display:flex;gap:26px;align-items:center;color:var(--ink)}
.topbar a{font-family:'Merriweather',serif;text-decoration:underline;display:flex;align-items:center;gap:6px}
.topbar .ther{color:var(--orange)}
.topbar .pat{color:var(--teal)}
.dot-icon{width:15px;height:15px;border-radius:50%;display:inline-block}
.nav-band{top:53px;height:31px;background:var(--navy)}
.nav{top:53px;left:622px;height:31px;display:flex;font-size:13px;color:#fff}
.nav span{display:flex;align-items:center;justify-content:center;width:125px}
.nav .active{background:var(--navy-dark);font-weight:600;width:95px}
.brand{top:28px;left:141px;width:170px;height:64px;background:#fff;padding:0 4px}
.brand .mark{display:flex;align-items:center;gap:10px;font-family:'Montserrat',sans-serif;font-weight:600;color:var(--navy)}
.brand .mark i{width:30px;height:30px;border-radius:50%;background:var(--teal);display:block}
.brand .name{font-size:36px;letter-spacing:12px;line-height:40px}
.brand .tag{font-size:8.5px;letter-spacing:1.2px;margin-top:4px;font-weight:600;color:var(--navy)}

/* hero */
.hero-photo{top:84px;left:0;width:1200px;height:529px;background:linear-gradient(90deg,#f7f5f1 0%,#f4ede2 35%,#efcf8f 60%,#d49a4a 80%,#b87a3e 100%)}
.hero-welcome{top:276px;left:142px;font-size:22px;color:var(--orange);font-weight:500}
.hero-title{top:312px;left:142px;font-size:44px;line-height:58px;color:var(--ink)}
.hero-title b{font-weight:700}
.login-card{top:538px;left:142px;width:916px;height:140px;background:#fff;border-left:3px solid var(--teal);box-shadow:0 4px 18px rgba(0,0,0,.12);border-radius:3px}
.login-card h3{position:absolute;left:50px;top:38px;font-size:18px;font-weight:400;color:var(--ink)}
.login-card h3 b{color:var(--navy);font-weight:700}
.login-card p{position:absolute;left:50px;top:70px;width:690px;font-size:13px;line-height:18px;color:var(--muted)}
.btn{display:flex;align-items:center;justify-content:center;color:#fff;font-weight:700;font-size:13px;letter-spacing:.5px;border-radius:2px}
.btn-orange{background:var(--orange)}
.btn-teal{background:var(--teal)}

/* section headings */
.dot-head{width:28px;height:28px;border-radius:50%;background:var(--teal);left:586px}
.h-center{left:0;width:1200px;text-align:center;font-family:'Merriweather',serif;font-weight:400;font-size:40px;color:var(--ink)}
.p-center{left:0;width:1200px;text-align:center;font-size:14px;line-height:21px;color:var(--ink)}

/* services */
.services-photo{top:995px;left:142px;width:436px;height:301px;background:linear-gradient(90deg,#d9b79a 0%,#c79c76 30%,#9eb3c9 60%,#7c96b3 100%)}
.services h2{font-family:'Merriweather',serif;font-size:22px;font-weight:700;color:var(--ink)}
.services p{margin-top:18px;width:380px;font-size:13.5px;line-height:21px;color:var(--muted)}
.services ul{list-style:none;margin-top:12px}
.services li{font-family:'Merriweather',serif;font-size:13px;display:flex;align-items:center;gap:16px;height:31px}
.services li i{width:10px;height:14px;background:var(--teal);border-radius:5px 5px 2px 2px;display:block}

/* staff */
.staff-band{top:1379px;left:0;width:1200px;height:599px;background:var(--navy)}
.staff-ghost{top:1390px;left:0;width:1200px;text-align:center;font-family:'Merriweather',serif;font-size:110px;font-weight:700;color:rgba(255,255,255,.04)}
.staff-title{top:1462px;color:#fff}
.staff-sub{top:1529px;color:#dfe8ef;font-size:17px}
.staff-card{top:1579px;width:211px;height:292px;background:#fff;text-align:center}
.staff-card .ph{height:154px;position:relative;overflow:hidden}
.staff-card svg{position:absolute;left:0;bottom:0}
.staff-card h4{font-family:'Merriweather',serif;font-weight:400;font-size:14px;margin-top:12px;color:var(--ink)}
.staff-card .role{font-size:10px;color:var(--teal);margin-top:3px}
.staff-card p{font-size:10px;line-height:13.5px;color:var(--muted);padding:0 16px;margin-top:7px}
.plus{width:22px;height:22px;border-radius:50%;background:var(--orange);color:#fff;font-size:18px;line-height:21px;margin:10px auto 0;font-weight:400}
.arrow{width:32px;height:32px;border-radius:50%;background:#fff;top:1716px}
.arrow svg{display:block;margin:9px}

/* helped */
.helped h2{font-family:'Merriweather',serif;font-weight:400;font-size:40px;line-height:49px;color:var(--ink)}
.helped p{margin-top:30px;width:350px;font-size:13.5px;line-height:21px;color:var(--ink)}
.video{top:2111px;left:573px;width:485px;height:283px;background:linear-gradient(135deg,#d8d4ce 0%,#c9b9a8 40%,#a69382 70%,#8b7a6c 100%)}
.play-label{top:2195px;left:1008px;font-family:'Merriweather',serif;font-weight:700;font-size:13px;color:#fff;transform:rotate(-90deg);transform-origin:left top;white-space:nowrap}
.play-line{left:1019px;top:2270px;width:1px;height:62px;background:var(--orange)}
.play-btn{left:996px;top:2335px;width:44px;height:44px;border-radius:50%;background:var(--orange)}

/* resources */
.res-card{top:2714px;width:288px;height:342px;border:1px solid var(--line);border-radius:6px;overflow:hidden;background:#fff}
.res-card .ph{height:224px}
.res-card .date{font-size:10px;color:var(--muted);margin:20px 0 0 26px}
.res-card h5{font-size:13.5px;font-weight:500;line-height:20px;margin:10px 26px 0;color:var(--ink)}
.res-card .more{font-family:'Merriweather',serif;font-size:12px;color:var(--orange);margin:10px 0 0 26px}

/* cta */
.cta-photo{top:3151px;left:0;width:588px;height:385px;background:linear-gradient(135deg,#f1f1f0 0%,#c7c9cb 40%,#8c8f92 70%,#e9e9e8 100%)}
.cta-panel{top:3151px;left:588px;width:612px;height:385px;background:var(--navy-dark)}
.cta-kicker{top:3231px;left:674px;display:flex;align-items:center;gap:10px;color:#fff;font-size:15px}
.cta-kicker i{width:20px;height:20px;border-radius:50%;background:var(--teal);display:block}
.cta-text{top:3272px;left:674px;width:360px;font-family:'Merriweather',serif;font-weight:300;font-size:23px;line-height:30px;color:#fff}

/* footer */
.footer-brand{top:3588px;left:102px}
.socials{top:3674px;left:100px;display:flex;gap:10px}
.socials i{width:26px;height:26px;border:1px solid #bbb;border-radius:50%;display:block}
.fcol h6{font-family:'Merriweather',serif;font-weight:400;font-size:15px;color:var(--ink)}
.fcol ul{list-style:none;margin-top:16px}
.fcol li{font-size:12.5px;line-height:30px;color:var(--ink)}
.fcol li::before{content:"› ";}
.fcol .login{font-family:'Merriweather',serif;font-size:12.5px;line-height:30px;display:flex;align-items:center;gap:8px;text-decoration:underline}
.foot-line{top:3760px;left:102px;width:995px;height:1px;background:var(--line)}
.copyright{top:3779px;left:0;width:1200px;text-align:center;font-size:12.5px;color:var(--ink)}
.copyright u{text-decoration:underline}
</style>
</head>
<body>

<!-- Header -->
<div class="abs nav-band" style="left:0;width:116px"></div>
<div class="abs nav-band" style="left:329px;width:871px"></div>
<div class="abs brand">
  <div class="mark"><i></i><span class="name">QMT</span></div>
  <div class="tag">QUIET MEADOW THERAPY</div>
</div>
<div class="abs topbar">
  <span>Login as a</span>
  <a class="ther"><span class="dot-icon" style="background:var(--orange)"></span>Therapists</a>
  <a class="pat"><span class="dot-icon" style="background:var(--teal)"></span>Patient</a>
</div>
<nav class="abs nav">
  <span class="active">Home</span><span>About</span><span>Services</span><span>Articles</span>
</nav>

<!-- Hero -->
<div class="abs hero-photo" role="img" aria-label="Smiling woman with curly hair looking up into warm sunlight"></div>
<div class="abs hero-welcome">Welcome To</div>
<h1 class="abs hero-title serif" style="font-weight:400">QUIET MEADOW<br><b>THERAPY</b></h1>

<section class="abs login-card">
  <h3><b>Login &nbsp;as a</b> lorem ipsum dolor sit amet, consectetur adipiscing elit.</h3>
  <p>Sit fermentum dui mauris egestas tristique pellentesque quis. Nibh ut natoque vestibulum fringilla consequat arcu non tortor. Nullam pulvinar feugiat id tortor risus pharetra.</p>
  <div class="abs btn btn-orange" style="left:748px;top:22px;width:128px;height:43px">THERAPIST</div>
  <div class="abs btn btn-teal" style="left:748px;top:75px;width:128px;height:43px">PATIENT</div>
</section>

<!-- Who we are -->
<div class="abs dot-head" style="top:759px"></div>
<h2 class="abs h-center" style="top:805px">Who We Are</h2>
<p class="abs p-center" style="top:864px;left:295px;width:610px">Lorem ipsum dolor sit amet, consectetur adipiscing elit. Nullam pulvinar feugiat id tortor risus pharetra. Sit fermentum dui mauris egestas tristique pellentesque quis. Nibh ut natoque vestibulum fringilla consequat arcu non tortor. Nullam pulvinar feugiat id tortor risus pharetra.</p>

<div class="abs services-photo" role="img" aria-label="Smiling woman in a denim shirt talking with a friend"></div>
<section class="abs services" style="top:1032px;left:641px">
  <h2>Services we provide</h2>
  <p>Lorem ipsum dolor sit amet, consectetur adipiscing elit. Nullam pulvinar feugiat id tortor risus pharetra. Sit fermentum dui mauris egestas tristique pellentesque.</p>
  <ul>
    <li><i></i>Individual Therapy</li>
    <li><i></i>Couple Therapy</li>
    <li><i></i>Group Therapy</li>
    <li><i></i>Teen Therapy</li>
  </ul>
</section>

<!-- Staff -->
<div class="abs staff-band"></div>
<div class="abs staff-ghost">Friendly Staff</div>
<h2 class="abs h-center staff-title">Our &nbsp;Friendly Staff</h2>
<p class="abs p-center staff-sub">Lorem ipsum dolor sit amet, consectetur adipiscing elit.</p>

<div class="abs arrow" style="left:85px"><svg width="14" height="14" viewBox="0 0 14 14"><path d="M9 2 4 7l5 5" fill="none" stroke="#f39200" stroke-width="2"/></svg></div>
<div class="abs arrow" style="left:1081px"><svg width="14" height="14" viewBox="0 0 14 14"><path d="M5 2l5 5-5 5" fill="none" stroke="#f39200" stroke-width="2"/></svg></div>

<div class="abs staff-card" style="left:142px">
  <div class="ph" role="img" aria-label="Portrait of a male therapist" style="background:linear-gradient(160deg,#e4e8ec,#b9a796)">
    <svg width="211" height="30" viewBox="0 0 211 30"><path d="M0 8 Q105 40 211 8 V30 H0Z" fill="#fff"/><path d="M0 8 Q105 40 211 8" fill="none" stroke="#1db1a2" stroke-width="4"/></svg>
  </div>
  <h4>Therapist Name</h4><div class="role">Expirience</div>
  <p>Lorem ipsum dolor sit amet, consectetur adipiscing elit. Nullam pulvinar feugiat id tortor.</p>
  <div class="plus">+</div>
</div>
<div class="abs staff-card" style="left:377px">
  <div class="ph" role="img" aria-label="Portrait of a female therapist among flowers" style="background:linear-gradient(160deg,#a9b98a,#e6cfa6)">
    <svg width="211" height="30" viewBox="0 0 211 30"><path d="M0 8 Q105 40 211 8 V30 H0Z" fill="#fff"/><path d="M0 8 Q105 40 211 8" fill="none" stroke="#1db1a2" stroke-width="4"/></svg>
  </div>
  <h4>Therapist Name</h4><div class="role">Expirience</div>
  <p>Lorem ipsum dolor sit amet, consectetur adipiscing elit. Nullam pulvinar feugiat id tortor.</p>
  <div class="plus">+</div>
</div>
<div class="abs staff-card" style="left:612px">
  <div class="ph" role="img" aria-label="Portrait of a smiling female therapist" style="background:linear-gradient(160deg,#eeeeee,#d6bfa4)">
    <svg width="211" height="30" viewBox="0 0 211 30"><path d="M0 8 Q105 40 211 8 V30 H0Z" fill="#fff"/><path d="M0 8 Q105 40 211 8" fill="none" stroke="#1db1a2" stroke-width="4"/></svg>
  </div>
  <h4>Therapist Name</h4><div class="role">Expirience</div>
  <p>Lorem ipsum dolor sit amet, consectetur adipiscing elit. Nullam pulvinar feugiat id tortor.</p>
  <div class="plus">+</div>
</div>
<div class="abs staff-card" style="left:847px">
  <div class="ph" role="img" aria-label="Portrait of a bearded male therapist with glasses" style="background:linear-gradient(160deg,#b8bcc0,#4a4644)">
    <svg width="211" height="30" viewBox="0 0 211 30"><path d="M0 8 Q105 40 211 8 V30 H0Z" fill="#fff"/><path d="M0 8 Q105 40 211 8" fill="none" stroke="#1db1a2" stroke-width="4"/></svg>
  </div>
  <h4>Therapist Name</h4><div class="role">Expirience</div>
  <p>Lorem ipsum dolor sit amet, consectetur adipiscing elit. Nullam pulvinar feugiat id tortor.</p>
  <div class="plus">+</div>
</div>

<!-- How we've helped -->
<section class="abs helped" style="top:2127px;left:142px">
  <h2>How We've<br>Helped</h2>
  <p>Lorem ipsum dolor sit amet, consectetur adipiscing elit. Nullam pulvinar feugiat id tortor risus pharetra. Sit fermentum dui mauris egestas tristique pellentesque quis. Nibh ut natoque vestibulum fringilla consequat arcu non tortor. Nullam pulvinar feugiat id tortor risus pharetra.</p>
</section>
<div class="abs video" role="img" aria-label="Therapist leading a group session with clients on a sofa"></div>
<div class="abs play-label">Play Video</div>
<div class="abs play-line"></div>
<div class="abs play-btn"><svg width="44" height="44" viewBox="0 0 44 44"><path d="M18 14v16l12-8z" fill="#fff"/></svg></div>

<!-- Resources -->
<div class="abs dot-head" style="top:2509px"></div>
<h2 class="abs h-center" style="top:2553px">Resourses For You</h2>
<p class="abs p-center" style="top:2620px;font-size:17px;line-height:28px">Lorem ipsum dolor sit amet, consectetur adipiscing elit<br>egestas tristique pellentesque quis.</p>

<article class="abs res-card" style="left:142px">
  <div class="ph" role="img" aria-label="Smiling blonde woman outdoors" style="background:linear-gradient(160deg,#8ea46a,#e9d3b5)"></div>
  <div class="date">01 &nbsp;Aug. 2022</div>
  <h5>Lorem ipsum dolor sit amet, ipsum consectetur adipiscing elit.</h5>
  <div class="more">Read More ⟶</div>
</article>
<article class="abs res-card" style="left:456px">
  <div class="ph" role="img" aria-label="Tired student resting head on a desk with pencils and papers" style="background:linear-gradient(160deg,#f0eeec,#cfc6bd)"></div>
  <div class="date">01 &nbsp;Aug. 2022</div>
  <h5>Lorem ipsum dolor sit amet, ipsum consectetur adipiscing elit.</h5>
  <div class="more">Read More ⟶</div>
</article>
<article class="abs res-card" style="left:770px">
  <div class="ph" role="img" aria-label="Stressed woman holding her head surrounded by papers and phones" style="background:linear-gradient(160deg,#d7d9dc,#8d7c74)"></div>
  <div class="date">01 &nbsp;Aug. 2022</div>
  <h5>Lorem ipsum dolor sit amet, ipsum consectetur adipiscing elit.</h5>
  <div class="more">Read More ⟶</div>
</article>

<!-- Login CTA -->
<div class="abs cta-photo" role="img" aria-label="Top view of a support group sitting in a circle"></div>
<div class="abs cta-panel"></div>
<div class="abs cta-kicker"><i></i>LOGIN AS</div>
<p class="abs cta-text">Lorem ipsum dolor sit amet, consectetur adipiscing elit. Sit fermentum dui mauris egestas tristique pellentesque quis.</p>
<div class="abs btn btn-orange" style="top:3418px;left:674px;width:126px;height:43px">THERAPIST</div>
<div class="abs btn btn-teal" style="top:3418px;left:822px;width:128px;height:43px">PATIENT</div>

<!-- Footer -->
<div class="abs footer-brand">
  <div style="display:flex;align-items:center;gap:10px;font-weight:600;color:var(--navy)"><i style="width:30px;height:30px;border-radius:50%;background:var(--teal);display:block"></i><span style="font-size:36px;letter-spacing:12px;line-height:40px">QMT</span></div>
  <div style="font-size:8.5px;letter-spacing:1.2px;margin-top:4px;font-weight:600;color:var(--navy)">QUIET MEADOW THERAPY</div>
</div>
<div class="abs socials"><i></i><i></i><i></i><i></i></div>

<div class="abs fcol" style="top:3584px;left:551px">
  <h6>Quick links</h6>
  <ul><li>Home</li><li>Services</li><li>Articles</li><li>About</li></ul>
</div>
<div class="abs fcol" style="top:3584px;left:736px">
  <h6>Services</h6>
  <ul><li>Individual Therapy</li><li>Couple Therapy</li><li>Group Therapy</li><li>Teen Therapy</li></ul>
</div>
<div class="abs fcol" style="top:3584px;left:963px">
  <h6>Login</h6>
  <div style="margin-top:12px">
    <div class="login" style="color:var(--orange)"><span class="dot-icon" style="background:var(--orange)"></span>Therapists</div>
    <div class="login" style="color:var(--teal)"><span class="dot-icon" style="background:var(--teal)"></span>Patient</div>
  </div>
</div>
<div class="abs foot-line"></div>
<div class="abs copyright">©Copyright 2022. <u>QUIET MEADOW THERAPY</u> | All Rights Reserved</div>

</body>
</html>
```